Dental marketing ad poster

I recently opened a new dental practice about 2 months ago and would like to have an ad designed for an A-frame poster to place outside our office. The goal of this ad is to attract and appeal to potential patients so they feel encouraged to come into the practice.
I’m leaving the creative direction up to you—I’d like to see what you can come up with. The ad can be funny or serious, but it should be eye-catching and patient-focused. Please highlight that we provide crowns, implants and teeth whitening.
My theme color is green but I’ll accept any color
Let me see your ideas!
Dentistry

```html
<!DOCTYPE html>
<html lang="en">
<head>
<meta charset="utf-8">
<title>Willowcreek Dentistry Poster</title>
<link rel="stylesheet" href="https://fonts.googleapis.com/css2?family=Playfair+Display:wght@700;800&family=Poppins:wght@400;500;600;700;800&display=swap">
<style>
:root{
  --blue:#1f56b3;
  --green:#1d9148;
  --mint:#c9efe9;
  --mint-light:#dcf4f0;
  --teal:#8fd9cc;
  --white:#ffffff;
  --stage:#a9a9a9;
}
*{margin:0;padding:0;box-sizing:border-box}
html,body{width:1033px;height:1200px;overflow:hidden;background:var(--stage)}
.poster{position:absolute;left:66px;top:18px;width:900px;height:1164px;background:var(--white);overflow:hidden;font-family:"Poppins",sans-serif}
.headline{position:absolute;left:0;right:0;top:46px;text-align:center;font-family:"Playfair Display",serif;font-weight:800;line-height:.98;letter-spacing:-1px}
.headline .blue{color:var(--blue);font-size:78px;display:block}
.headline .green{color:var(--green);font-size:84px;display:block}
.headline .gap{margin-top:10px}
.wave{position:absolute;left:0;top:440px;width:900px;height:500px}
.lower-band{position:absolute;left:0;top:928px;width:900px;height:130px;background:var(--mint-light)}
.photo{position:absolute;background:var(--white);padding:7px;box-shadow:0 3px 8px rgba(0,0,0,.25)}
.photo .fill{width:100%;height:100%}
.photo-one{left:50px;top:405px;width:196px;height:212px;transform:rotate(5deg)}
.photo-one .fill{background:linear-gradient(135deg,#c9b7a8,#e9e4de 55%,#4fc3c7)}
.photo-two{left:262px;top:404px;width:196px;height:214px;transform:rotate(-5deg)}
.photo-two .fill{background:linear-gradient(160deg,#eef1f3,#d6dde3 50%,#9fb8d6)}
.portrait{position:absolute;left:583px;top:330px;width:317px;height:598px;background:linear-gradient(180deg,rgba(255,255,255,0) 0%,#e5c1a8 30%,#d9ad91 70%,#efe4dc 100%);border-radius:150px 150px 0 0}
.services-title{position:absolute;left:42px;top:660px;font-size:28px;font-weight:800;letter-spacing:-.3px;color:var(--green)}
.services-title span{color:var(--blue)}
.service{position:absolute;left:64px;height:61px;background:var(--blue);border-radius:14px 0 0 14px;color:var(--white);padding:8px 0 0 36px}
.service small{display:block;font-size:15.5px;font-weight:500;line-height:1.1}
.service strong{display:block;font-size:23px;font-weight:800;line-height:1.15}
.service-crowns{top:709px;width:541px}
.service-implants{top:788px;width:553px;padding-left:41px}
.service-whitening{top:867px;width:565px;padding-left:41px}
.service-icon{position:absolute;left:41px;width:44px;height:44px}
.brand{position:absolute;left:40px;top:980px;width:250px;text-align:center;color:var(--green);font-weight:600;font-size:30px;line-height:1.05}
.brand em{font-style:normal;display:block;font-size:17px;letter-spacing:6px;margin-top:4px}
.cta{position:absolute;left:327px;top:968px;font-size:23.5px;font-weight:800;line-height:1.38;color:var(--blue);letter-spacing:-.2px}
.cta span{color:var(--green)}
.footer{position:absolute;left:0;top:1056px;width:900px;height:108px;background:var(--green);color:var(--white)}
.contact{position:absolute;display:flex;align-items:center;gap:6px;white-space:nowrap}
.contact svg{flex:none}
.phone{left:40px;top:22px;font-size:27px;font-weight:700}
.address{left:40px;top:62px;font-size:17.5px;font-weight:500}
.email{left:500px;top:26px;font-size:18px}
.web{left:500px;top:55px;font-size:18px}
</style>
</head>
<body>
<main class="poster">
  <svg class="wave" viewBox="0 0 900 500" preserveAspectRatio="none" aria-hidden="true">
    <path d="M0 30 C150 110 300 120 450 90 S750 40 900 30 L900 500 L0 500 Z" fill="var(--mint)"/>
    <path d="M0 0 C120 70 260 100 420 85 C560 70 700 30 840 10 L840 18 C700 40 560 82 420 98 C260 112 120 90 0 30 Z" fill="var(--teal)"/>
    <path d="M0 22 C140 90 300 110 450 90 S750 40 900 30" fill="none" stroke="var(--white)" stroke-width="5"/>
  </svg>
  <div class="lower-band"></div>

  <h1 class="headline">
    <span class="blue">YOUR SMILE</span>
    <span class="blue">IS OUR PASSION AT</span>
    <span class="green gap">WILLOWCREEK</span>
    <span class="green">DENTISTRY</span>
  </h1>

  <figure class="photo photo-one"><div class="fill" role="img" aria-label="Surprised patient in a dental chair with a dentist nearby"></div></figure>
  <figure class="photo photo-two"><div class="fill" role="img" aria-label="Dentist performing a teeth whitening treatment with a curing light"></div></figure>
  <div class="portrait" role="img" aria-label="Smiling young woman with hands framing her face"></div>

  <h2 class="services-title">WHAT WE DO <span>BEST</span></h2>

  <div class="service service-crowns"><small>RENEW YOUR SMILE WITH</small><strong>PORCELAIN CROWNS</strong></div>
  <div class="service service-implants"><small>DISCOVER LASTING SOLUTIONS WITH</small><strong>DENTAL IMPLANTS</strong></div>
  <div class="service service-whitening"><small>ACHIEVE A DAZZLING LOOK WITH</small><strong>PROFESSIONAL TEETH WHITENING</strong></div>

  <svg class="service-icon" style="top:718px" viewBox="0 0 44 44" aria-hidden="true"><circle cx="22" cy="22" r="21" fill="var(--green)" stroke="var(--white)" stroke-width="2"/><path d="M14 15c0-3 4-4 8-2 4-2 8-1 8 2 0 4-2 6-2 10 0 4-2 6-3 3-1-3-2-4-3-4s-2 1-3 4c-1 3-3 1-3-3 0-4-2-6-2-10z" fill="none" stroke="var(--white)" stroke-width="1.6"/></svg>
  <svg class="service-icon" style="top:797px" viewBox="0 0 44 44" aria-hidden="true"><circle cx="22" cy="22" r="21" fill="var(--green)" stroke="var(--white)" stroke-width="2"/><path d="M15 13c0-2 3-3 7-1 4-2 7-1 7 1 0 3-2 5-3 7h-8c-1-2-3-4-3-7z" fill="none" stroke="var(--white)" stroke-width="1.6"/><path d="M19 22h6M19 26h6M20 30h4M22 30v4" stroke="var(--white)" stroke-width="1.6"/></svg>
  <svg class="service-icon" style="top:876px" viewBox="0 0 44 44" aria-hidden="true"><circle cx="22" cy="22" r="21" fill="var(--green)" stroke="var(--white)" stroke-width="2"/><path d="M13 16c0-3 4-4 8-2 4-2 8-1 8 2 0 4-2 6-2 10 0 4-2 6-3 3-1-3-2-4-3-4s-2 1-3 4c-1 3-3 1-3-3 0-4-2-6-2-10z" fill="none" stroke="var(--white)" stroke-width="1.6"/><path d="M31 9v6M28 12h6" stroke="var(--white)" stroke-width="1.6"/></svg>

  <div class="brand">Willowcreek<em>— DENTISTRY —</em></div>

  <p class="cta">Ready for a Brighter <span>Healthier Smile?</span><br>Schedule Your Consultation Today!</p>

  <footer class="footer">
    <div class="contact phone"><svg width="16" height="16" viewBox="0 0 16 16" aria-hidden="true"><circle cx="8" cy="8" r="8" fill="var(--blue)"/><path d="M5 4.5l1.6-.4.9 2-1 .8c.5 1 1.2 1.7 2.2 2.2l.8-1 2 .9-.4 1.6c-3.3 0-6.1-2.8-6.1-6.1z" fill="var(--white)"/></svg>(555) 014-2380</div>
    <div class="contact address"><svg width="16" height="16" viewBox="0 0 16 16" aria-hidden="true"><path d="M8 1a5 5 0 0 1 5 5c0 4-5 9-5 9S3 10 3 6a5 5 0 0 1 5-5z" fill="var(--blue)"/><circle cx="8" cy="6" r="2" fill="var(--white)"/></svg>2450 Maple Row Ste 210 Riverton, TN 37000</div>
    <div class="contact email"><svg width="14" height="14" viewBox="0 0 14 14" aria-hidden="true"><circle cx="7" cy="7" r="7" fill="var(--blue)"/><rect x="3.5" y="4.5" width="7" height="5" fill="none" stroke="var(--white)" stroke-width="1"/></svg>hello@willowcreekdentalcare.com</div>
    <div class="contact web"><svg width="14" height="14" viewBox="0 0 14 14" aria-hidden="true"><circle cx="7" cy="7" r="7" fill="var(--blue)"/><circle cx="7" cy="7" r="3.5" fill="none" stroke="var(--white)" stroke-width="1"/><path d="M3.5 7h7" stroke="var(--white)" stroke-width="1"/></svg>willowcreekdentalcare.com</div>
  </footer>
</main>
</body>
</html>
```